Business Card Design

We are a motorcycle parts, spares, accessories and workshop as well as a vq dealership. We mostly specialize in dirt bikes. I have uploaded a pic of bikes lined up at the starting gate. I envisage having the picture as a backboard maybe out of focus with the logo at the top of the card and the details off to the right side.

Target Market(s)

Male Motorcycle enthusiast aged 18-35

Industry/Entity Type

Business

Contact Information for Business Card

7/318 Banksia Hollow Rd
Carrow Ridge QLD 4118
Ph: (07) 3482 9157
Email: maree@trailgearsupply.com.au
www.trailgearsupply.com.au

Requirements
Must have
• on the rear side of the card lines for writing

```html
<!DOCTYPE html>
<html lang="en">
<head>
<meta charset="utf-8">
<title>Banksia Trail Gear – Business Card</title>
<link rel="stylesheet" href="https://fonts.googleapis.com/css2?family=Open+Sans:wght@400;700&display=swap">
<style>
  :root {
    --page-bg: #e9e7e4;
    --ink-light: #ffffff;
    --tag-ink: #2a2a30;
    --photo-red: #c8475c;
    --photo-pink: #d98a9c;
    --photo-sky: #a9b8dc;
    --photo-grey: #8d9189;
    --photo-teal: #3f6a5e;
    --band: rgba(28, 52, 46, 0.55);
    --strip: rgba(255, 255, 255, 0.28);
    --note-box: rgba(255, 255, 255, 0.32);
    --note-line: #3a3a3a;
  }
  * { box-sizing: border-box; margin: 0; padding: 0; }
  html, body {
    width: 1200px;
    height: 1000px;
    overflow: hidden;
    background: var(--page-bg);
    font-family: "Open Sans", Arial, sans-serif;
  }
  .card {
    position: absolute;
    left: 75px;
    top: 200px;
    width: 1050px;
    height: 600px;
    overflow: hidden;
    box-shadow: 0 10px 30px rgba(0,0,0,0.25);
  }
  .card__photo {
    position: absolute;
    inset: 0;
    background:
      radial-gradient(ellipse 40% 35% at 85% 5%, var(--photo-sky), transparent 70%),
      radial-gradient(ellipse 45% 40% at 60% 45%, var(--photo-red), transparent 75%),
      radial-gradient(ellipse 35% 30% at 20% 20%, var(--photo-pink), transparent 75%),
      radial-gradient(ellipse 30% 40% at 10% 70%, var(--photo-teal), transparent 75%),
      radial-gradient(ellipse 40% 30% at 45% 85%, var(--photo-pink), transparent 75%),
      linear-gradient(160deg, #b9a3ad 0%, var(--photo-grey) 55%, #b8aab0 100%);
  }
  .card__brand {
    position: absolute;
    left: 150px;
    top: 48px;
    display: flex;
    align-items: center;
    gap: 22px;
  }
  .brand__name {
    font-weight: 700;
    font-size: 68px;
    letter-spacing: 1px;
    text-transform: uppercase;
    color: var(--ink-light);
    line-height: 1;
    white-space: nowrap;
  }
  .brand__mark {
    width: 46px;
    height: 46px;
    background: var(--ink-light);
  }
  .card__tagline {
    position: absolute;
    left: 380px;
    top: 150px;
    font-weight: 700;
    font-size: 30px;
    letter-spacing: 3px;
    text-transform: uppercase;
    color: var(--tag-ink);
    white-space: nowrap;
  }
  .card__band {
    position: absolute;
    left: 0;
    top: 220px;
    width: 100%;
    height: 240px;
    background: var(--band);
    border-top: 2px solid rgba(255,255,255,0.35);
  }
  .card__strip {
    position: absolute;
    left: 0;
    top: 460px;
    width: 100%;
    height: 140px;
    background: var(--strip);
  }
  .contact {
    position: absolute;
    left: 70px;
    top: 238px;
    list-style: none;
    color: var(--ink-light);
    font-size: 28px;
    line-height: 44px;
    white-space: nowrap;
  }
  .notes {
    position: absolute;
    left: 570px;
    top: 405px;
    width: 430px;
    height: 160px;
    background: var(--note-box);
    border: 1px solid rgba(255,255,255,0.55);
  }
  .notes__line {
    position: absolute;
    left: 30px;
    right: 30px;
    height: 1px;
    background: var(--note-line);
  }
  .notes__line--first { top: 58px; }
  .notes__line--second { top: 110px; }
</style>
</head>
<body>
  <article class="card">
    <div class="card__photo" role="img" aria-label="Out-of-focus photo of dirt bikes lined up at the starting gate"></div>

    <header class="card__brand">
      <span class="brand__name">Banksia Trail Gear</span>
      <span class="brand__mark"></span>
    </header>
    <p class="card__tagline">Repairs - Sales - Service</p>

    <div class="card__band"></div>
    <div class="card__strip"></div>

    <ul class="contact">
      <li>7/318 Banksia Hollow Rd Carrow Ridge QLD 4118</li>
      <li>Ph: (07) 3482 9157</li>
      <li>Email:maree@trailgearsupply.com.au</li>
      <li>www.trailgearsupply.com.au</li>
    </ul>

    <div class="notes" aria-label="Space for writing">
      <span class="notes__line notes__line--first"></span>
      <span class="notes__line notes__line--second"></span>
    </div>
  </article>
</body>
</html>
```